Natural Cosmetics need a Packaging Design

We need a PACKAGING design for labels on hand/body wash bottles and soap paper boxes.
We target at high end markets.
We expect a contemporary and trendy design.
We don't need a separate logo. The brand name "Va Mirel" acts as the logo.
We want a modern and classic font for "Va Mirel".
Please see attached pictures for packaging samples.

Industry/Entity Type

Cosmetics

Requirements
Should not have
• a separate logo from the brand name

```html
<!DOCTYPE html>
<html lang="en">
<head>
<meta charset="utf-8">
<title>Va Mirel — Rose and Herbs Packaging</title>
<link rel="stylesheet" href="https://fonts.googleapis.com/css2?family=Cinzel:wght@400&family=Oswald:wght@300&family=Playfair+Display:ital@1&display=swap">
<style>
  :root {
    --bg: #1d2108;
    --white: #ffffff;
    --ink: #1a1a1a;
    --olive: #9aa82a;
    --olive-light: #c9d66a;
    --olive-dark: #4f5a0c;
    --band-black: #0b0b0b;
    --magenta: #c0186b;
    --magenta-dark: #5a0c33;
  }
  * { margin: 0; padding: 0; box-sizing: border-box; }
  html, body { width: 1200px; height: 1200px; overflow: hidden; }
  body {
    background: var(--bg);
    position: relative;
    font-family: "Cinzel", serif;
  }
  .brand-mark {
    position: absolute;
    left: 110px; top: 150px;
    font-family: "Cinzel", serif;
    font-weight: 400;
    font-size: 74px;
    letter-spacing: 2px;
    color: var(--white);
  }

  .label {
    position: absolute;
    background: var(--white);
    overflow: hidden;
  }
  .label--shower { left: 480px; top: 300px; width: 320px; height: 540px; }
  .label--hand   { left: 850px; top: 600px; width: 290px; height: 300px; }
  .label--box    { left: 90px;  top: 600px; width: 330px; height: 330px; }

  .label__pattern {
    position: absolute;
    border-radius: 50%;
    background: radial-gradient(ellipse at center, rgba(154,168,42,0.55) 0%, rgba(154,168,42,0.25) 45%, rgba(255,255,255,0) 70%);
  }

  .label__brand {
    position: absolute;
    left: 0; right: 0;
    text-align: center;
    font-family: "Cinzel", serif;
    font-size: 16px;
    color: var(--ink);
  }

  .label__band {
    position: absolute;
    left: 0; right: 0;
    background: linear-gradient(90deg, var(--olive-light) 0%, var(--olive) 18%, var(--olive-dark) 40%, var(--band-black) 62%, var(--band-black) 100%);
    color: var(--white);
    font-family: "Oswald", sans-serif;
    font-weight: 300;
    text-align: center;
    letter-spacing: 3px;
    display: flex;
    align-items: center;
    justify-content: center;
  }
  .label__accent {
    position: absolute;
    height: 22px;
    background: linear-gradient(90deg, var(--magenta) 0%, var(--magenta-dark) 100%);
    transform: skewX(-40deg);
  }

  .label__scent {
    position: absolute;
    left: 0; right: 0;
    text-align: center;
    font-family: "Playfair Display", serif;
    font-style: italic;
    letter-spacing: 4px;
    color: var(--ink);
  }
  .label__volume {
    position: absolute;
    left: 0; right: 0;
    text-align: center;
    font-family: "Oswald", sans-serif;
    font-weight: 300;
    color: var(--ink);
  }
</style>
</head>
<body>

  <div class="brand-mark">VA MIREL</div>

  <!-- Shower gel label -->
  <section class="label label--shower">
    <div class="label__pattern" role="img" aria-label="Olive dotted wave pattern" style="left:-60px; top:20px; width:260px; height:240px;"></div>
    <div class="label__pattern" role="img" aria-label="Olive dotted wave pattern" style="left:120px; top:300px; width:260px; height:260px;"></div>
    <div class="label__brand" style="top:52px; font-size:18px;">VA MIREL</div>
    <div class="label__band" style="top:130px; height:110px; font-size:46px;">SHOWER GEL</div>
    <div class="label__accent" style="left:50px; top:240px; width:130px;"></div>
    <div class="label__scent" style="top:368px; font-size:19px;">rose and herbs</div>
    <div class="label__volume" style="top:476px; font-size:14px;">500ML</div>
  </section>

  <!-- Hand soap label -->
  <section class="label label--hand">
    <div class="label__pattern" role="img" aria-label="Olive dotted wave pattern" style="left:-30px; top:-20px; width:230px; height:180px;"></div>
    <div class="label__pattern" role="img" aria-label="Olive dotted wave pattern" style="left:20px; top:170px; width:260px; height:160px;"></div>
    <div class="label__brand" style="top:42px; font-size:15px;">VA MIREL</div>
    <div class="label__band" style="top:100px; height:80px; font-size:38px;">HAND SOAP</div>
    <div class="label__accent" style="left:50px; top:180px; width:100px; height:16px;"></div>
    <div class="label__scent" style="top:218px; font-size:15px;">rose and herbs</div>
    <div class="label__volume" style="top:262px; font-size:11px;">300ML</div>
  </section>

  <!-- Body soap box top -->
  <section class="label label--box">
    <div class="label__pattern" role="img" aria-label="Olive dotted wave pattern" style="left:-40px; top:10px; width:260px; height:140px;"></div>
    <div class="label__pattern" role="img" aria-label="Olive radiating dotted pattern" style="left:70px; top:130px; width:300px; height:220px;"></div>
    <div class="label__brand" style="top:40px; font-size:14px;">VA MIREL</div>
    <div class="label__band" style="top:120px; height:70px; font-size:34px;">BODYSOAP</div>
    <div class="label__accent" style="left:60px; top:190px; width:100px; height:16px;"></div>
    <div class="label__scent" style="top:222px; font-size:14px;">rose and herbs</div>
    <div class="label__volume" style="top:262px; font-size:12px;">120g</div>
    <div class="label__brand" style="top:300px; font-size:11px;">VA MIREL</div>
  </section>

</body>
</html>
```